Vital Spark Electrical in need of a business card design

We need a new business card designed for our electrical business. We have a logo already which I will attach below.
Would like the business card to be..
-BLACK background preferably, possibly white back ground behind logo if colours clash.
-White & Blue (logo blue) text
Something that makes the logo pop, & a modern look. Possibly minimal clean format.

REQUIRE:
-Logo on front & back

TEXT TO INCLUDE (ON ONE SIDE):

Tom Harlow
Director/Electrician
M: 0417 365 208
E:info@vitalsparkelectrical-example.com.au
W:www.vitalsparkelectrical-example.com.au
R.E.C 57318

Custom/New Homes
Renovations
Commercial Office/Shop Fit-outs
Communications & Security Cameras
Electric Vehicle Chargers
Airconditioning
Updates

Requirements
Nice to have
• Possibly even lighten the grey shades for the words 'Vital' & 'Spark' to be more easily read on a black background.

```html
<!DOCTYPE html>
<html lang="en">
<head>
<meta charset="utf-8">
<title>Vital Spark Electrical – Business Card</title>
<link rel="stylesheet" href="https://fonts.googleapis.com/css2?family=Montserrat:wght@400;500;600&display=swap">
<style>
  :root {
    --page: #e4e4e4;
    --card-light: #ffffff;
    --card-dark: #2f3b46;
    --ink: #2f3b46;
    --ink-soft: #4f5963;
    --blue: #0fa8e0;
    --white: #ffffff;
  }
  * { box-sizing: border-box; margin: 0; padding: 0; }
  html, body {
    width: 1200px; height: 1028px; overflow: hidden;
    background: var(--page);
    font-family: "Montserrat", sans-serif;
  }
  .canvas { position: relative; width: 1200px; height: 1028px; }

  .card {
    position: absolute; left: 310px; width: 579px; height: 331px;
    border-radius: 22px; overflow: hidden;
  }
  .card--front { top: 165px; background: var(--card-light); }
  .card--back { top: 532px; background: var(--card-dark); }

  .brand {
    position: absolute; display: flex; align-items: center; gap: 10px;
    font-weight: 600; white-space: nowrap;
  }
  .brand__mark { display: block; background: var(--blue); }
  .card--front .brand {
    left: 0; right: 0; top: 40px; justify-content: center;
    font-size: 27px; color: var(--ink);
  }
  .card--front .brand__mark { width: 22px; height: 22px; }
  .card--back .brand {
    right: 32px; bottom: 34px; font-size: 17px; color: var(--white);
  }
  .card--back .brand__mark { width: 14px; height: 14px; }

  .details {
    position: absolute; left: 0; right: 0; top: 160px;
    display: flex; justify-content: center; align-items: center; gap: 18px;
    white-space: nowrap;
  }
  .person { text-align: right; }
  .person__name {
    font-size: 21px; font-weight: 500; color: var(--blue);
    letter-spacing: .8px; line-height: 1;
  }
  .person__role {
    margin-top: 6px; font-size: 12.5px; color: var(--ink-soft); letter-spacing: .2px;
  }
  .divider { width: 2px; height: 56px; background: var(--blue); flex: none; }
  .contacts { list-style: none; }
  .contacts li {
    display: flex; align-items: center; gap: 8px;
    height: 20px; font-size: 12.5px; color: var(--ink-soft); letter-spacing: .1px;
  }
  .contacts svg { width: 11px; height: 11px; flex: none; }

  .licence-bar {
    position: absolute; left: 0; right: 0; top: 285px; height: 14px;
    display: flex; align-items: center;
  }
  .licence-bar__dark { width: 228px; height: 11px; background: var(--ink); }
  .licence-bar__blue { flex: 1; height: 11px; background: var(--blue); }
  .licence-bar__text {
    padding: 0 7px; font-size: 18px; font-weight: 500; color: var(--ink);
    letter-spacing: .5px; line-height: 1; white-space: nowrap;
  }
  .licence-bar__text span { color: var(--blue); }

  .services {
    position: absolute; left: 0; right: 0; top: 89px; list-style: none;
    text-align: center;
  }
  .services li {
    height: 26px; line-height: 26px; font-size: 19px; letter-spacing: .6px;
    color: var(--white); white-space: nowrap;
  }
  .services li:nth-child(even) { color: var(--blue); }
</style>
</head>
<body>
<main class="canvas">

  <section class="card card--front" aria-label="Card front">
    <div class="brand"><span class="brand__mark"></span>Vital Spark Electrical</div>

    <div class="details">
      <div class="person">
        <p class="person__name">TOM HARLOW</p>
        <p class="person__role">Director/Electrician</p>
      </div>
      <span class="divider"></span>
      <ul class="contacts">
        <li>
          <svg viewBox="0 0 12 12" aria-hidden="true"><path d="M3 1 L4.6 3.6 L3.6 4.6 Q4.8 7.4 7.4 8.4 L8.4 7.4 L11 9 L10 11 Q4 11 1 3 Z" fill="none" stroke="#0fa8e0" stroke-width="1.2" stroke-linejoin="round"/></svg>
          0417 365 208
        </li>
        <li>
          <svg viewBox="0 0 12 12" aria-hidden="true"><rect x="1" y="2.5" width="10" height="7" rx="1" fill="none" stroke="#0fa8e0" stroke-width="1.2"/><path d="M1.5 3 L6 6.5 L10.5 3" fill="none" stroke="#0fa8e0" stroke-width="1.2"/></svg>
          info@vitalsparkelectrical-example.com.au
        </li>
        <li>
          <svg viewBox="0 0 12 12" aria-hidden="true"><g fill="none" stroke="#0fa8e0" stroke-width="1"><circle cx="6" cy="6" r="5"/><ellipse cx="6" cy="6" rx="2.2" ry="5"/><path d="M1 6 H11 M2 3.5 H10 M2 8.5 H10"/></g></svg>
          www.vitalsparkelectrical-example.com.au
        </li>
      </ul>
    </div>

    <div class="licence-bar">
      <span class="licence-bar__dark"></span>
      <p class="licence-bar__text"><span>R.E.C</span> 57318</p>
      <span class="licence-bar__blue"></span>
    </div>
  </section>

  <section class="card card--back" aria-label="Card back">
    <ul class="services">
      <li>Renovations</li>
      <li>Custom/New Homes</li>
      <li>Commercial Office/Shop Fit-outs</li>
      <li>Communications &amp; Security Cameras</li>
      <li>Electric Vehicle Chargers</li>
      <li>Airconditioning</li>
    </ul>
    <div class="brand"><span class="brand__mark"></span>Vital Spark Electrical</div>
  </section>

</main>
</body>
</html>
```